Townhome Multi-Family Property Exterior Sign

Hello. We are looking for a new design for our exterior pylon for for a multi-family housing property in Texas. The design will need to go on a new sign panel to replace the existing (see photo of existing). We are looking to see both modern and contemporary designs. Included the sign should be the name, Loma Brisa Townhomes and the web address www.lomabrisatownhomes.example.

Attached here is a PDF file of the proposed new sign shape. We are open to other shape ideas as well if your design would better suit a more rectangular shape.

Industry/Entity Type

Property

Font styles to use
Serif
Sans Serif

Colors
9bcb3c

Requirements
Must have
• Name of building: Loma Brisa Townhomes
• Website: www.lomabrisatownhomes.example
Nice to have
• Address: 420-530 Halvorsen Lane (only if it fits nicely)

```html
<!DOCTYPE html>
<html lang="en">
<head>
<meta charset="utf-8">
<title>Loma Brisa Townhomes — Exterior Sign Panel</title>
<link rel="stylesheet" href="https://fonts.googleapis.com/css2?family=Allura&family=Montserrat:wght@700&display=swap">
<style>
  :root {
    --panel-green: #9bcb3c;
    --deep-green: #0f7a3c;
    --script-green: #12793a;
    --white: #ffffff;
    --backdrop: #f3f5ef;
  }
  html, body {
    margin: 0;
    padding: 0;
    width: 1200px;
    height: 998px;
    overflow: hidden;
    background: var(--backdrop);
  }
  .canvas {
    position: relative;
    width: 1200px;
    height: 998px;
  }
  .sign-panel {
    position: absolute;
    left: 50px;
    top: 230px;
    width: 1100px;
    height: 540px;
  }
  .sign-shape {
    position: absolute;
    inset: 0;
    width: 1100px;
    height: 540px;
  }
  .sign-shape path {
    fill: var(--panel-green);
    stroke: var(--deep-green);
    stroke-width: 18;
    stroke-linejoin: round;
  }
  .property-name {
    position: absolute;
    left: 0;
    right: 0;
    top: 118px;
    margin: 0;
    text-align: center;
    font-family: "Allura", cursive;
    font-weight: 400;
    font-size: 230px;
    line-height: 1;
    color: var(--script-green);
    white-space: nowrap;
  }
  .property-type {
    position: absolute;
    left: 170px;
    top: 343px;
    width: 810px;
    height: 70px;
    background: var(--deep-green);
    display: flex;
    align-items: center;
    justify-content: center;
    font-family: "Montserrat", sans-serif;
    font-weight: 700;
    font-size: 52px;
    letter-spacing: 0.36em;
    padding-left: 0.36em;
    box-sizing: border-box;
    color: var(--white);
  }
  .website {
    position: absolute;
    left: 0;
    right: 0;
    top: 448px;
    text-align: center;
    font-family: "Montserrat", sans-serif;
    font-weight: 700;
    font-size: 38px;
    letter-spacing: 0.08em;
    color: var(--white);
    white-space: nowrap;
  }
</style>
</head>
<body>
  <main class="canvas">
    <section class="sign-panel" aria-label="Loma Brisa Townhomes sign">
      <svg class="sign-shape" viewBox="0 0 1100 540" aria-hidden="true">
        <path d="M9,124 C240,124 330,9 560,9 C800,9 900,128 1091,140 L1091,531 L9,531 Z"/>
      </svg>
      <h1 class="property-name">Loma Brisa</h1>
      <div class="property-type">TOWNHOMES</div>
      <div class="website">WWW.LOMABRISATOWNHOMES.EXAMPLE</div>
    </section>
  </main>
</body>
</html>
```